New Lead input page design

Attached is our concept of a new lead input screen for the back-end of our website which is a tool for a loan agent (2 page PDF attached)

1. This is the first of many other data input screen projects for our website, so the designer that ends up with us will have quite a bit of add on new projects.

2. HERE IS THE LINK WITH THE SAMPLE OF ALL THE CURRENT CONTROLS:
http://apps.brimtally88.net/controlWidgets.html

3. The colors and hues of: either GREEN & GREYS or BLUE & GREYS.

4. I think some gradients and shadows adds depth and sophistication. Basically trying to get away from old school flat, one dimensional data screen inputs and add some design flare to it.

5. Upon completion we will need the HTML of the design etc and we will code the input fields directly.

6. See attached files for the entire input screen. Please also add the data input space (see sample) to your design.

Thank you

Reason: We are extending the deadline to give us time to ask current designs to complete slight revisions

Reason: Finalizing the selection for one last variation detailed to current designers

```html
<!DOCTYPE html>
<html lang="en">
<head>
<meta charset="utf-8">
<title>New Lead Input</title>
<link rel="stylesheet" href="https://fonts.googleapis.com/css2?family=Arimo:wght@400;700&display=swap">
<style>
:root{
  --page:#f6f6f6;
  --card:#ffffff;
  --card-fade:#f1f1f1;
  --nav-top:#3b95e8;
  --nav-bottom:#1d75d8;
  --nav-active:#1a66c9;
  --label:#222222;
  --value:#3a3a3a;
  --green:#3aa10f;
  --rule:#cfd3d8;
  --rule-blue:#b9cde3;
  --col-rule:#e3e3e3;
}
*{box-sizing:border-box;margin:0;padding:0}
html,body{width:960px;height:1200px;overflow:hidden}
body{background:var(--page);font-family:"Arimo",Arial,sans-serif;font-size:12px;color:var(--value);position:relative}
.tabs{position:absolute;left:96px;top:0;width:768px;height:81px;background:linear-gradient(var(--nav-top),var(--nav-bottom));display:flex;list-style:none}
.tab{position:absolute;top:7px;width:105px;height:59px;display:flex;flex-direction:column;align-items:center;justify-content:flex-end;padding-bottom:11px;color:#fff;font-size:11px;letter-spacing:-.2px;text-transform:uppercase}
.tab svg{width:22px;height:22px;margin-bottom:6px}
.tab.active{background:var(--nav-active);border-radius:3px;box-shadow:inset 0 1px 2px rgba(0,0,0,.15)}
.lead{position:absolute;left:96px;top:103px;width:768px;height:1068px;background:var(--card);box-shadow:0 1px 4px rgba(0,0,0,.08)}
.section{display:flex;background:linear-gradient(var(--card) 55%,var(--card-fade));border-bottom:1px solid var(--rule)}
.section.blue{border-bottom-color:var(--rule-blue)}
.side{width:146px;border-right:1px solid var(--col-rule);display:flex;flex-direction:column;align-items:center;padding-top:20px}
.badge{width:48px;height:48px;border-radius:6px}
.side h2{font-size:12px;font-weight:700;color:var(--label);margin-top:8px;letter-spacing:.2px}
.col{padding:16px 0 0 30px;border-right:1px solid var(--col-rule)}
.col.left{width:299px}
.col.right{flex:1;border-right:none}
.row{display:flex;height:22.5px;align-items:center}
.row.gap{margin-top:7.5px}
.row dt{font-weight:700;color:var(--label);width:112px}
.col.right .row dt{width:133px}
.add{color:var(--green);font-weight:700}
.u{text-decoration:underline}
</style>
</head>
<body>
<ul class="tabs">
  <li class="tab active" style="left:30px">
    <svg viewBox="0 0 24 24"><path fill="#fff" d="M12 2l3 6.5 7 .8-5.2 4.8 1.5 7L12 17.5 5.7 21l1.5-7L2 9.3l7-.8z"/></svg>Lead Category</li>
  <li class="tab" style="left:160px">
    <svg viewBox="0 0 24 24"><path fill="#fff" d="M5 2h10l5 5v15H5z"/><path fill="#1d75d8" d="M15 2v5h5z" opacity=".4"/></svg>Sticky Note</li>
  <li class="tab" style="left:278px">
    <svg viewBox="0 0 24 24"><path fill="#fff" d="M3 7h4l2-3h6l2 3h4v13H3z"/><circle cx="12" cy="13" r="4" fill="#2a84de"/><circle cx="12" cy="13" r="2.3" fill="#fff"/></svg>Snap Shot</li>
  <li class="tab" style="left:393px">
    <svg viewBox="0 0 24 24"><path fill="#fff" d="M12 2l11 20H1z"/><rect x="11" y="9" width="2" height="7" fill="#2a84de"/><rect x="11" y="17.5" width="2" height="2" fill="#2a84de"/></svg>Alerts</li>
  <li class="tab" style="left:511px">
    <svg viewBox="0 0 24 24"><path fill="none" stroke="#fff" stroke-width="2" d="M14 4H4v17h15V11"/><path fill="#fff" d="M19 2l3 3-10 10H9v-3z"/></svg>Lead Notes</li>
  <li class="tab" style="left:632px">
    <svg viewBox="0 0 24 24"><rect x="3" y="4" width="18" height="18" fill="none" stroke="#fff" stroke-width="2"/><rect x="3" y="4" width="18" height="4" fill="#fff"/><path fill="#fff" d="M6 11h3v2H6zm4.5 0h3v2h-3zm4.5 0h3v2h-3zM6 15h3v2H6zm4.5 0h3v2h-3zm4.5 0h3v2h-3zM6 19h3v1H6z"/><rect x="7" y="1" width="2" height="5" fill="#fff"/><rect x="15" y="1" width="2" height="5" fill="#fff"/></svg>Calendar</li>
</ul>

<main class="lead">
  <section class="section" style="height:213px">
    <div class="side"><div class="badge" role="img" aria-label="Client person icon" style="background:linear-gradient(#e9c9a6,#c9821e)"></div><h2>CLIENTS</h2></div>
    <dl class="col left">
      <div class="row"><dt>Borrower 1</dt><dd>Daniel Hartwell</dd></div>
      <div class="row"><dt>Phone</dt><dd>555-010-2234</dd></div>
      <div class="row gap"><dt>Borrower 2</dt><dd>Grace Hartwell</dd></div>
      <div class="row"><dt>Phone</dt><dd>555-010-2234</dd></div>
      <div class="row gap"><dt>Application</dt><dd>Joint</dd></div>
      <div class="row"><dt>New Title Holders</dt><dd>Joint</dd></div>
      <div class="row"><dt>Lead Status</dt><dd><span class="u">3</span>&nbsp; Demo : &nbsp;<span class="u">4</span></dd></div>
    </dl>
    <dl class="col right">
      <div class="row"><dt>Address</dt><dd>418 Orchard Ln., Fairbrook, CA</dd></div>
      <div class="row"><dt>E-mail</dt><dd>daniel@mailnest.com</dd></div>
      <div class="row gap"><dt>Address</dt><dd>418 Orchard Ln., Fairbrook, CA</dd></div>
      <div class="row"><dt>E-mail</dt><dd>grace@mailnest.com</dd></div>
      <div class="row gap"><dt>Relationship</dt><dd>Husband &amp; Wife</dd></div>
      <div class="row"><dt class="add">Add Borrowers</dt></div>
    </dl>
  </section>

  <section class="section blue" style="height:125px">
    <div class="side"><div class="badge" role="img" aria-label="Loan document with coins icon" style="background:linear-gradient(#eeeeee,#c99a3a)"></div><h2>EXISTING LOAN</h2></div>
    <dl class="col left">
      <div class="row"><dt>Current Amount</dt><dd>$335,758</dd></div>
      <div class="row"><dt>Current Loan</dt><dd>30 year fix - 5.5%</dd></div>
      <div class="row"><dt>Approx Last Refi</dt><dd>4 years ago</dd></div>
      <div class="row"><dt>How many loans</dt><dd>2 &nbsp;<b style="color:var(--label)">Pay off both?</b> Yes</dd></div>
    </dl>
    <dl class="col right">
      <div class="row"><dt>Current P &amp; I</dt><dd>$2,200</dd></div>
      <div class="row"><dt>Tax &amp; Insurance</dt><dd>$450</dd></div>
      <div class="row"><dt>Total Payment</dt><dd>$2,650</dd></div>
      <div class="row"><dt class="add">Add More Loans</dt></div>
    </dl>
  </section>

  <section class="section blue" style="height:125px">
    <div class="side"><div class="badge" role="img" aria-label="New loan document with coins icon" style="background:linear-gradient(#e8f0e2,#c99a3a)"></div><h2>NEW LOAN</h2></div>
    <dl class="col left">
      <div class="row"><dt>New Amount</dt><dd>$336,000</dd></div>
      <div class="row"><dt>New Loan</dt><dd>30 year fix - <span class="add">select</span></dd></div>
      <div class="row"><dt>Quoted Rate</dt><dd>5%</dd></div>
      <div class="row"><dt>LTV</dt><dd>75%</dd></div>
    </dl>
    <dl class="col right">
      <div class="row"><dt>New Loan Purpose</dt><dd>Rate &amp; Term</dd></div>
      <div class="row"><dt>Closing Cost</dt><dd>$450</dd></div>
      <div class="row"><dt>Lender Credit</dt><dd>$450</dd></div>
      <div class="row"><dt>CLTV</dt><dd>70%</dd></div>
    </dl>
  </section>

  <section class="section" style="height:214px">
    <div class="side"><div class="badge" role="img" aria-label="Hand holding credit card icon" style="background:linear-gradient(#f1c9a0,#9cc77a)"></div><h2>CREDIT</h2></div>
    <dl class="col left">
      <div class="row"><dt>Borrower 1</dt><dd>Daniel Hartwell</dd></div>
      <div class="row"><dt>DOB</dt><dd>02/22/1975</dd></div>
      <div class="row"><dt>Social</dt><dd>900-11-2345</dd></div>
      <div class="row"><dt>Estimated Credit</dt><dd>Excellent</dd></div>
      <div class="row"><dt>Credit Pull Date</dt><dd>04/28/2014</dd></div>
      <div class="row"><dt>Credit Age</dt><dd>2 Days</dd></div>
      <div class="row"><dt>Credit Score</dt><dd>700 688 744</dd></div>
      <div class="row"><dt>DTI</dt><dd>44%-32%</dd></div>
    </dl>
    <dl class="col right">
      <div class="row"><dt>Borrower 2</dt><dd>Grace Hartwell</dd></div>
      <div class="row"><dt>DOB</dt><dd>01/25/1973</dd></div>
      <div class="row"><dt>Social</dt><dd>900-22-6789</dd></div>
      <div class="row"><dt>Estimated Credit</dt><dd>Excellent</dd></div>
      <div class="row"><dt>Credit Pull Date</dt><dd>04/28/14</dd></div>
      <div class="row"><dt>Credit Age</dt><dd>2 Days</dd></div>
      <div class="row"><dt>Credit Score</dt><dd>712 694 708</dd></div>
      <div class="row"><dt>Qualified Score</dt><dd>688</dd></div>
    </dl>
  </section>

  <section class="section" style="height:147px">
    <div class="side"><div class="badge" role="img" aria-label="House icon" style="background:linear-gradient(#8a5a3c,#f2f2f2)"></div><h2>PROPERTY</h2></div>
    <dl class="col left">
      <div class="row"><dt>Properties</dt><dd>2</dd></div>
      <div class="row"><dt>Subject Property</dt><dd>418 Orchard Ln., Fairbrook, CA</dd></div>
      <div class="row"><dt>Purpose</dt><dd>Primary</dd></div>
      <div class="row"><dt>Appraised Value</dt><dd>$405,000</dd></div>
      <div class="row"><dt>Year Built</dt><dd>1981</dd></div>
    </dl>
    <dl class="col right">
      <div class="row"><dt class="add">Add Property</dt></div>
      <div class="row"><dt>Residence Term</dt><dd>5 years</dd></div>
      <div class="row"><dt>Property Type</dt><dd>SFR</dd></div>
      <div class="row"><dt>Approximate Value</dt><dd>$445,000</dd></div>
      <div class="row"><dt>HOA</dt><dd>No</dd></div>
    </dl>
  </section>

  <section class="section" style="height:244px;border-bottom:none">
    <div class="side"><div class="badge" role="img" aria-label="Stack of money icon" style="background:linear-gradient(#a9d48a,#4f7a3a)"></div><h2>INCOME</h2></div>
    <dl class="col left">
      <div class="row"><dt>Income Source 1</dt><dd>Employment</dd></div>
      <div class="row"><dt>Employer</dt><dd>Tallow Works</dd></div>
      <div class="row"><dt>Address</dt><dd>72 Linden way</dd></div>
      <div class="row"><dt>Work Phone</dt><dd>555-010-7788</dd></div>
      <div class="row"><dt>Position</dt><dd>Admin</dd></div>
      <div class="row"><dt>Length</dt><dd>2 years</dd></div>
      <div class="row"><dt>Term</dt><dd>3 years</dd></div>
      <div class="row"><dt>Gross Income</dt><dd>$3,000</dd></div>
      <div class="row"><dt class="add">Add Other Income</dt></div>
    </dl>
    <dl class="col right">
      <div class="row"><dt>Income Source 1</dt><dd>Employment</dd></div>
      <div class="row"><dt>Employer</dt><dd>Tallow Works</dd></div>
      <div class="row"><dt>Address</dt><dd>72 Linden way</dd></div>
      <div class="row"><dt>Work Phone</dt><dd>555-010-7788</dd></div>
      <div class="row"><dt>Position</dt><dd>Manager</dd></div>
      <div class="row"><dt>Length</dt><dd>4 years</dd></div>
      <div class="row"><dt>Term</dt><dd>2 years</dd></div>
      <div class="row"><dt>Gross Monthly Income</dt><dd>$4,500</dd></div>
      <div class="row"><dt class="add">Add Other Income</dt></div>
    </dl>
  </section>
</main>
</body>
</html>
```